Looking for a clean, modern, and professional business card design that reflects Valtrim Systems

The design should include the company logo, contact details, and align with our brand identity. Please use a sophisticated and minimalist style, incorporating [specific colors, if applicable]. Creativity is welcome, but the card must maintain a polished and professional appearance.

Details to Include:

Name: Gavin Trelowe
Title: VP Sales / Operations
Company: Valtrim Systems
Phone: 483.216.7705
Email: gavin@valtrimsystems-example.com
Website: www.valtrimsystems-example.com

```html
<!DOCTYPE html>
<html lang="en">
<head>
<meta charset="UTF-8">
<title>Valtrim Systems — Business Card</title>
<link href="https://fonts.googleapis.com/css2?family=Montserrat:wght@400;500;700;800&display=swap" rel="stylesheet">
<style>
  :root {
    --brand-blue: #3a73b3;
    --ink: #111111;
    --card: #ffffff;
    --backdrop: #e4e4e2;
  }
  * { margin: 0; padding: 0; box-sizing: border-box; }
  html, body { width: 1200px; height: 801px; overflow: hidden; }
  body {
    background: var(--backdrop);
    font-family: "Montserrat", sans-serif;
    color: var(--ink);
    display: flex;
    align-items: center;
    justify-content: center;
    gap: 60px;
  }
  .card {
    position: relative;
    width: 530px;
    height: 303px;
    background: var(--card);
    border-bottom: 3px solid var(--brand-blue);
    box-shadow: 0 10px 30px rgba(0,0,0,0.12);
    overflow: hidden;
  }
  /* Front */
  .front .wordmark {
    position: absolute;
    left: 34px;
    top: 40px;
    font-size: 30px;
    font-weight: 800;
    letter-spacing: 1px;
    color: var(--ink);
  }
  .front .accent-bar {
    position: absolute;
    left: 0;
    top: 150px;
    width: 22px;
    height: 44px;
    background: var(--brand-blue);
  }
  .front .person {
    position: absolute;
    left: 42px;
    top: 148px;
  }
  .person-name {
    font-size: 20px;
    font-weight: 800;
    color: var(--brand-blue);
    line-height: 1.1;
  }
  .person-title {
    font-size: 14px;
    font-weight: 500;
    margin-top: 4px;
  }
  .contacts {
    position: absolute;
    left: 42px;
    top: 222px;
    list-style: none;
    font-size: 12px;
    font-weight: 500;
    line-height: 1.7;
  }
  .contacts li { display: flex; align-items: center; gap: 8px; }
  .contacts svg { width: 12px; height: 12px; fill: var(--brand-blue); flex: none; }
  .front .decor-square {
    position: absolute;
    right: 50px;
    top: 30px;
    width: 150px;
    height: 150px;
    background: var(--brand-blue);
  }
  .front .company-tag {
    position: absolute;
    right: 26px;
    bottom: 22px;
    font-size: 11px;
    font-weight: 500;
  }
  /* Back */
  .back {
    display: flex;
    align-items: center;
    justify-content: center;
  }
  .back .wordmark {
    font-size: 46px;
    font-weight: 800;
    letter-spacing: 1px;
    color: var(--ink);
  }
</style>
</head>
<body>
  <section class="card front">
    <div class="wordmark">Valtrim Systems</div>
    <div class="decor-square"></div>
    <div class="accent-bar"></div>
    <div class="person">
      <div class="person-name">Gavin Trelowe</div>
      <div class="person-title">VP Sales / Operations</div>
    </div>
    <ul class="contacts">
      <li>
        <svg viewBox="0 0 24 24" aria-hidden="true"><path d="M6.6 10.8a15 15 0 0 0 6.6 6.6l2.2-2.2a1 1 0 0 1 1-.25 11.4 11.4 0 0 0 3.6.57 1 1 0 0 1 1 1V20a1 1 0 0 1-1 1A17 17 0 0 1 3 4a1 1 0 0 1 1-1h3.5a1 1 0 0 1 1 1c0 1.25.2 2.45.57 3.57a1 1 0 0 1-.25 1z"/></svg>
        483.216.7705
      </li>
      <li>
        <svg viewBox="0 0 24 24" aria-hidden="true"><path d="M2 5h20v14H2zm2 2v.5l8 5 8-5V7l-8 5z"/></svg>
        gavin@valtrimsystems-example.com
      </li>
      <li>
        <svg viewBox="0 0 24 24" aria-hidden="true"><circle cx="12" cy="12" r="10"/></svg>
        www.valtrimsystems-example.com
      </li>
    </ul>
    <div class="company-tag">Valtrim Systems</div>
  </section>

  <section class="card back">
    <div class="wordmark">Valtrim Systems</div>
  </section>
</body>
</html>
```